Sturdyflow Mechanical - Letterhead

We are a plumbing and hvac company based in Calgary. This letterhead will be on our quotes, invoices, preventative maintenance proposals etc.

```html
<!DOCTYPE html>
<html lang="en">
<head>
<meta charset="utf-8">
<title>Sturdyflow Mechanical – Letterhead</title>
<link rel="stylesheet" href="https://fonts.googleapis.com/css2?family=Open+Sans:wght@400;600;700&family=Arimo:wght@700&display=swap">
<style>
  :root {
    --backdrop: #e3e4e6;
    --paper: #f8f8f8;
    --ink: #2b2b2b;
    --ink-soft: #3a3a3a;
    --brand-blue: #2f6fb8;
    --brand-orange: #e9542a;
  }
  * { box-sizing: border-box; margin: 0; padding: 0; }
  html, body {
    width: 1200px; height: 945px; overflow: hidden;
    background: var(--backdrop);
  }
  .letterhead {
    position: absolute;
    left: 260px; top: 28px;
    width: 680px; height: 880px;
    background: var(--paper);
    box-shadow: 0 6px 24px rgba(0,0,0,0.12);
    font-family: "Open Sans", sans-serif;
    color: var(--ink);
  }
  .brand {
    position: absolute; left: 64px; top: 78px;
    display: flex; align-items: center; gap: 10px;
  }
  .brand-dot {
    width: 26px; height: 26px; border-radius: 50%;
    background: var(--brand-orange);
  }
  .brand-name {
    font-weight: 700; font-size: 21px; line-height: 1;
    color: var(--brand-blue); letter-spacing: 0.3px;
  }
  .contact {
    position: absolute; right: 64px; top: 56px;
    font-size: 9px; line-height: 1.35; color: var(--ink-soft);
    font-style: normal;
  }
  .contact-address { margin-bottom: 5px; }
  .contact-list { list-style: none; }
  .contact-list li { display: flex; align-items: center; gap: 5px; }
  .contact-icon {
    width: 9px; height: 9px; border-radius: 50%;
    background: var(--brand-orange);
    display: inline-flex; align-items: center; justify-content: center;
    flex: none;
  }
  .letter-body {
    position: absolute; left: 82px; top: 238px; width: 540px;
  }
  .salutation {
    font-family: "Arimo", sans-serif; font-weight: 700;
    font-size: 14px; margin-bottom: 14px; color: #111;
  }
  .letter-body p {
    font-size: 12px; line-height: 1.4; color: var(--ink-soft);
    margin: 0 0 18px 14px;
  }
  .signature {
    position: absolute; left: 96px; top: 660px;
    width: 130px; height: 44px;
    background: linear-gradient(90deg, #ececec, #e2e2e2);
    border-radius: 4px;
  }
  .footer-band {
    position: absolute; left: 0; bottom: 0;
    width: 100%; height: 8px; background: var(--brand-blue);
  }
</style>
</head>
<body>
  <main class="letterhead">
    <header>
      <div class="brand">
        <span class="brand-dot"></span>
        <span class="brand-name">STURDYFLOW MECHANICAL</span>
      </div>
      <address class="contact">
        <div class="contact-address">Po. Box 56, Street Name,<br>City Name, Zip Code - 00000</div>
        <ul class="contact-list">
          <li><span class="contact-icon"><svg width="5" height="5" viewBox="0 0 10 10"><path d="M2 1l2 2-1 1.5a6 6 0 0 0 2.5 2.5L7 6l2 2-1.5 1.5C4 9 1 6 0.5 2.5z" fill="#fff"/></svg></span>855-555-0142</li>
          <li><span class="contact-icon"><svg width="5" height="5" viewBox="0 0 10 10"><rect x="1" y="2" width="8" height="6" fill="none" stroke="#fff" stroke-width="1.4"/><path d="M1 2l4 3 4-3" fill="none" stroke="#fff" stroke-width="1.2"/></svg></span>info@sturdyflowmechanical.com</li>
          <li><span class="contact-icon"><svg width="5" height="5" viewBox="0 0 10 10"><circle cx="5" cy="5" r="4" fill="none" stroke="#fff" stroke-width="1.4"/><path d="M1 5h8M5 1v8" stroke="#fff" stroke-width="1"/></svg></span>www.sturdyflowmechanical.com</li>
        </ul>
      </address>
    </header>

    <section class="letter-body">
      <h2 class="salutation">Dear Mr. Harlow,</h2>
      <p>Lorem Ipsum is simply dummy text of the printing and typesetting industry. Lorem Ipsum has been the industry's standard dummy text ever since the 1500s, when an unknown printer took a galley of type and scrambled it to make a type specimen book. It has survived not only five centuries, but also the leap into electronic typesetting, remaining essentially unchanged.</p>
      <p>The standard chunk of Lorem Ipsum used since the 1500s is reproduced below for those interested. Sections 1.10.32 and 1.10.33 from "de Finibus Bonorum et Malorum" by Aldo Quintell are also reproduced in their exact original form, accompanied by English versions from the 1914 translation by H. Ashby</p>
      <p>Lorem Ipsum is simply dummy text of the printing and typesetting industry. Lorem Ipsum has been the industry's standard dummy text ever since the 1500s, when an unknown printer took a galley of type and scrambled it to make a type specimen book. It has survived not only five centuries, but also the leap into electronic typesetting, remaining essentially unchanged. It was popularised in the</p>
      <p>The standard chunk of Lorem Ipsum used since the 1500s is reproduced below for those interested. Sections 1.10.32 and 1.10.33 from "de Finibus Bonorum et Malorum" by Aldo Quintell are also reproduced in their exact original form, accompanied by English versions from the 1914 translation by H. Ashby</p>
    </section>

    <div class="signature" role="img" aria-label="Handwritten signature of the sender"></div>

    <div class="footer-band"></div>
  </main>
</body>
</html>
```